Create Premium Wine Label Design

We are premium wine exporters from Australia. We are looking to introduce new brand " The Velloro" - in red wine, White wine and Sparkling wine to international market.

The sample label design for red wine ( Shiraz) is attached.

This is our luxury brand. We need a stunning wine label designs for (front, back and neck) that should be mostly in GOLD colour and design should be really eye catching.

We have provided sample design for front, back and neck labels. However, we are looking forward to see a completely new improvised design.

LOGO attached.

Front Label Design Specification:

* We would like to see designs that are in Gold colour.
* Wine Bottle size is standard: 750ml; we assume the same design can be resizable to different bottle sizes.
* Our design should suit both black, white and sparkling wine bottles(sample attached)
* Use our logo in the design (see attached - label sample)
* Content for front label (see attached).
* Design should include all information specified in the sample

Back Label Design
* All contents in the sample should be used ( sample attached)
* LOGO attached.

Neck Label Design
* Sample of Neck label attached, please provide similar or your own design.
* LOGO attached.

Image Samples:
* Samples of label designs we like (see attached)
* Sample for gold color (see attached)
* For bottle shapes (see attached)
* Front, Back and Neck Label Samples (see attached)

Target Market(s)

International Wine Market

Font styles to use
Decorative
Script

Requirements
Must have
• Must have golden color on front and back label

```html
<!DOCTYPE html>
<html lang="en">
<head>
<meta charset="utf-8">
<title>Shiraz The Velloro – Label Set</title>
<link href="https://fonts.googleapis.com/css2?family=Cinzel:wght@600&family=Great+Vibes&family=Fredoka:wght@600&family=Crimson+Text:ital@1&family=Montserrat:wght@700&display=swap" rel="stylesheet">
<style>
:root{
  --black:#050505;
  --gold-light:#f7e3a0;
  --gold:#d9b45a;
  --gold-deep:#a8782a;
  --brown:#3a2208;
  --brown-dark:#1e1104;
  --red:#df2a44;
  --red-text:#f9e4b8;
  --white:#ffffff;
}
*{margin:0;padding:0;box-sizing:border-box}
html,body{width:1031px;height:1200px;overflow:hidden;background:var(--white)}
.canvas{position:relative;width:1031px;height:1200px}

.label{position:absolute;border-radius:58px;overflow:hidden;border:2px solid var(--gold)}
.front-label{left:55px;top:112px;width:428px;height:646px;background:var(--black)}
.back-label{left:539px;top:112px;width:428px;height:646px;background:var(--black)}

.gold-field{background:linear-gradient(100deg,var(--gold-deep) 0%,var(--gold) 20%,var(--gold-light) 50%,var(--gold) 80%,var(--gold-deep) 100%)}
.abs{position:absolute}
.center{left:0;right:0;text-align:center}

.brand-name{font-family:"Cinzel",serif;font-weight:600;color:var(--gold);letter-spacing:1px;white-space:nowrap}
.brand-mark{display:inline-block;width:14px;height:14px;border-radius:50%;background:var(--gold);vertical-align:middle;margin-right:8px}

.ornament{position:absolute;background:linear-gradient(90deg,rgba(217,180,90,0),var(--gold),rgba(217,180,90,0));border-radius:8px}

.wine-name{font-family:"Great Vibes",cursive;color:var(--brown);line-height:1}
.wine-sub{font-family:"Fredoka",sans-serif;font-weight:600;color:var(--red);text-transform:uppercase;line-height:1;letter-spacing:1px;white-space:nowrap}

/* front */
.front-top{top:0;left:0;right:0;height:185px}
.front-gold{top:180px;left:0;right:0;height:394px;clip-path:polygon(0 2%,25% 0,55% 3%,80% 0,100% 2%,100% 100%,0 100%)}
.front-pattern{inset:0;background:radial-gradient(circle at 50% 50%,rgba(255,245,200,.35),rgba(168,120,42,.15))}
.vintage-ribbon{left:115px;top:462px;width:200px;height:86px;border-radius:18px;background:linear-gradient(90deg,var(--brown),var(--gold-deep),var(--gold-light),var(--gold-deep));display:flex;align-items:center;justify-content:center}
.vintage-year{font-family:"Cinzel",serif;font-weight:600;font-size:30px;color:var(--brown-dark)}
.origin-line{font-family:"Great Vibes",cursive;font-size:28px;line-height:1;color:var(--gold)}

/* back */
.back-top{top:0;left:0;right:0;height:182px}
.back-story{top:179px;left:0;right:0;height:160px;background:var(--red);padding:16px 22px 0;clip-path:polygon(0 4%,20% 0,45% 3%,70% 0,100% 3%,100% 100%,0 100%)}
.back-story p{font-family:"Crimson Text",serif;font-style:italic;font-size:15.5px;line-height:20px;color:var(--red-text);text-align:center}
.origin-band{top:337px;left:0;right:0;height:48px;display:flex;align-items:center;justify-content:space-between;padding:0 34px 0 38px}
.origin-band span{font-family:"Montserrat",sans-serif;font-weight:700;font-size:19px;color:var(--brown-dark);letter-spacing:.5px}
.origin-mark{width:22px;height:22px;border-radius:50%;background:var(--red)}
.back-pattern{top:385px;left:0;right:0;bottom:0;background:radial-gradient(ellipse at 50% 30%,#2a2a2a,var(--black) 75%)}
.back-notes{top:418px;width:170px;font-family:"Crimson Text",serif;font-style:italic;font-size:12.5px;line-height:15.5px;color:#e8e8e8;text-align:center}
.back-notes.left{left:30px}
.back-notes.right{left:228px}
.info-box{left:92px;top:528px;width:242px;height:84px;background:var(--white)}

/* neck */
.neck-label{position:absolute;left:213px;top:822px;width:649px;height:180px;background:var(--black)}
.neck-pattern{left:0;right:0;height:40px;background:linear-gradient(90deg,var(--gold-deep),var(--gold-light),var(--gold),var(--gold-light),var(--gold-deep))}
.neck-pattern.top{top:0}
.neck-pattern.bottom{bottom:0}
.neck-rule{left:0;right:0;height:5px;background:var(--gold)}
.neck-band{left:0;right:0;top:50px;height:80px;background:linear-gradient(180deg,var(--brown-dark),var(--brown) 50%,var(--brown-dark))}
.neck-brand{top:18px;width:240px;text-align:center;font-size:24px}
</style>
</head>
<body>
<div class="canvas">

  <!-- Front label -->
  <section class="label front-label">
    <div class="abs front-top">
      <div class="abs center brand-name" style="top:98px;font-size:28px"><span class="brand-mark"></span>KESTRELLE</div>
      <div class="ornament" style="left:134px;top:146px;width:160px;height:10px" role="img" aria-label="Gold scroll ornament beneath the brand name"></div>
    </div>
    <div class="abs front-gold gold-field">
      <div class="abs front-pattern" role="img" aria-label="Gold damask pattern background with a brown swirl flourish"></div>
    </div>
    <div class="abs center wine-name" style="top:262px;font-size:124px">Shiraz</div>
    <div class="abs wine-sub" style="left:136px;top:394px;font-size:34px">The Velloro</div>
    <div class="abs vintage-ribbon" role="img" aria-label="Bronze scroll ribbon with the vintage year"><span class="vintage-year">2018</span></div>
    <div class="abs center origin-line" style="top:594px">Wine of Australia</div>
  </section>

  <!-- Back label -->
  <section class="label back-label">
    <div class="abs back-top gold-field">
      <div class="abs center wine-name" style="top:14px;font-size:100px">Shiraz</div>
      <div class="abs wine-sub" style="left:158px;top:124px;font-size:27px">The Velloro</div>
    </div>
    <div class="abs back-story">
      <p>Lorem ipsum dolor sit amet, consectetuer adipiscing elit, sed diam nonummy nibh euismod tincidunt ut laoreet dolore magna aliquam erat volutpat. Lorem ipsum dolor sit amet, consectetuer adipiscing elit, sed diam nonummy nibh euismod tincidunt ut laoreet dolore magna aliquam erat volutpat. Lorem ipsum dolor sit amet, consectetuer</p>
    </div>
    <div class="abs origin-band gold-field">
      <span>PRODUCT OF AUSTRALIA</span>
      <div class="origin-mark"></div>
    </div>
    <div class="abs back-pattern" role="img" aria-label="Dark charcoal damask pattern background"></div>
    <p class="abs back-notes left">Lorem ipsum dolor sit amet, consectetuer adipiscing elit, sed diam nonummy nibh euismod tincidunt ut laoreet dolore magna aliquam erat volutpat. Ut wisi enim ad minim veniam,</p>
    <p class="abs back-notes right">Lorem ipsum dolor sit amet, consectetuer adipiscing elit, sed diam nonummy nibh euismod tincidunt ut laoreet dolore magna aliquam erat volutpat. Ut wisi enim ad minim veniam,</p>
    <div class="abs info-box"></div>
  </section>

  <!-- Neck label -->
  <section class="neck-label">
    <div class="abs neck-pattern top" role="img" aria-label="Gold and black lace pattern strip"></div>
    <div class="abs neck-rule" style="top:42px"></div>
    <div class="abs neck-band">
      <div class="abs brand-name neck-brand" style="left:18px"><span class="brand-mark"></span>KESTRELLE</div>
      <div class="ornament" style="left:78px;top:56px;width:120px;height:8px" role="img" aria-label="Gold scroll ornament"></div>
      <div class="abs brand-name neck-brand" style="left:394px"><span class="brand-mark"></span>KESTRELLE</div>
      <div class="ornament" style="left:454px;top:56px;width:120px;height:8px" role="img" aria-label="Gold scroll ornament"></div>
    </div>
    <div class="abs neck-rule" style="top:133px"></div>
    <div class="abs neck-pattern bottom" role="img" aria-label="Gold and black lace pattern strip"></div>
  </section>

</div>
</body>
</html>
```